Logo, Web and Mobile Designs for enterprise social media platform

All the details are in the attached document, please start reading the scope document first which explains what is this project about and the details about the needed deliverables, after that please read the UI_Requirements document which will detail what is expected regarding the coded web version since this is a coded contest, it is very important that you meet the UI requirements or suggest something else but we will need to agree first before working on the coded version

Good Luck

Target Market(s)

Enterprise Social Media

Industry/Entity Type

Media

Coding

Coded - Design and coding required

Number of Pages Required

5+ page

Font styles to use
Sans Serif

Requirements
Must have
• All the must haves are listed in the scope document so please check before you start

```html
<!DOCTYPE html>
<html lang="en">
<head>
<meta charset="UTF-8">
<title>Teamora – Social Media Platform</title>
<link rel="stylesheet" href="https://fonts.googleapis.com/css2?family=Raleway:wght@400;500;600;700;800&family=Open+Sans:wght@400;600&display=swap">
<style>
  :root {
    --brand-blue: #1a6fcf;
    --brand-blue-dark: #1558b0;
    --accent-green: #5ccf2c;
    --accent-green-dark: #46b71c;
    --ink: #2b2b2b;
    --muted: #8a8a8a;
    --line: #c8c8c8;
    --white: #ffffff;
    --hero-a: #6f6b69;
    --hero-b: #b3a497;
    --hero-c: #8c8682;
    --social: #4a4f57;
  }
  * { box-sizing: border-box; margin: 0; padding: 0; }
  html, body { width: 1200px; height: 645px; overflow: hidden; background: var(--white); }
  body { position: relative; font-family: "Raleway", sans-serif; color: var(--ink); }

  .site-header { position: absolute; left: 0; top: 0; width: 1200px; height: 100px; }
  .brand { position: absolute; left: 97px; top: 34px; display: flex; align-items: center; gap: 10px; }
  .brand-dot { width: 30px; height: 30px; border-radius: 50%; background: var(--brand-blue); }
  .brand-name { font-family: "Raleway", sans-serif; font-weight: 800; font-size: 23px; color: var(--ink); letter-spacing: .2px; }

  .search { position: absolute; left: 323px; top: 29px; width: 352px; height: 38px; border: 1px solid var(--line); border-radius: 3px; display: flex; align-items: center; padding: 0 14px; }
  .search-input { flex: 1; font-family: "Raleway", sans-serif; font-size: 13px; color: var(--muted); }
  .search svg { width: 15px; height: 15px; }

  .quick-actions { position: absolute; top: 15px; left: 0; }
  .quick-action { position: absolute; width: 90px; margin-left: -45px; text-align: center; }
  .quick-icon { width: 38px; height: 33px; margin: 0 auto; border: 2px solid var(--muted); border-radius: 6px; display: flex; align-items: center; justify-content: center; }
  .quick-icon svg { width: 16px; height: 16px; fill: var(--muted); }
  .quick-label { font-size: 12.5px; font-weight: 500; color: var(--muted); line-height: 14px; margin-top: 10px; }

  .auth { position: absolute; top: 34px; height: 29px; border-radius: 3px; color: var(--white); font-size: 13px; font-weight: 600; display: flex; align-items: center; justify-content: center; gap: 4px; }
  .auth svg { width: 10px; height: 10px; fill: var(--white); }
  .auth-signin { left: 956px; width: 68px; background: var(--brand-blue-dark); }
  .auth-signup { left: 1033px; width: 68px; background: var(--accent-green); }

  .main-nav { position: absolute; left: 0; top: 100px; width: 1200px; height: 46px; background: var(--brand-blue); }
  .nav-item { position: absolute; top: 0; height: 46px; display: flex; align-items: center; justify-content: center; font-size: 13px; font-weight: 700; color: var(--white); border-left: 1px solid rgba(0,0,0,.12); }
  .nav-item.is-active { color: var(--accent-green); }
  .nav-item.is-last { border-right: 1px solid rgba(0,0,0,.12); }
  .nav-secondary { position: absolute; top: 0; height: 46px; display: flex; align-items: center; font-size: 13px; font-weight: 500; color: var(--white); }

  .hero { position: absolute; left: 0; top: 146px; width: 1200px; height: 415px; overflow: hidden; }
  .hero-media { position: absolute; inset: 0; background:
      radial-gradient(ellipse at 70% 45%, var(--hero-b) 0%, rgba(179,164,151,0) 60%),
      linear-gradient(100deg, var(--hero-a) 0%, var(--hero-c) 45%, var(--hero-b) 100%); }
  .hero-media::after { content: ""; position: absolute; inset: 0; background: rgba(120,120,120,.35); }
  .hero-copy { position: absolute; left: 0; width: 1200px; text-align: center; color: var(--white); text-shadow: 0 2px 3px rgba(0,0,0,.25); }
  .hero-kicker { top: 128px; font-size: 35px; font-weight: 600; letter-spacing: .5px; }
  .hero-title { top: 172px; font-size: 43px; font-weight: 800; letter-spacing: .3px; }
  .hero-cta { position: absolute; left: 527px; top: 236px; width: 147px; height: 43px; background: linear-gradient(var(--accent-green), var(--accent-green-dark)); border-radius: 2px; color: var(--white); font-size: 14px; font-weight: 700; display: flex; align-items: center; justify-content: center; }
  .hero-dots { position: absolute; top: 356px; left: 561px; display: flex; gap: 6px; }
  .hero-dot { width: 15px; height: 15px; border-radius: 50%; border: 2px solid var(--white); }
  .hero-dot.is-active { background: var(--accent-green); }

  .site-footer { position: absolute; left: 0; top: 561px; width: 1200px; height: 84px; font-family: "Open Sans", sans-serif; color: #555; }
  .copyright { position: absolute; left: 99px; top: 25px; font-size: 12.5px; }
  .footer-links { position: absolute; left: 98px; top: 47px; font-size: 12.5px; }
  .footer-links span { margin: 0 7px; }
  .social { position: absolute; left: 897px; top: 32px; display: flex; gap: 13px; }
  .social-item { width: 23px; height: 23px; border-radius: 3px; background: var(--social); }
</style>
</head>
<body>
  <header class="site-header">
    <div class="brand"><span class="brand-dot"></span><span class="brand-name">TEAMORA</span></div>

    <div class="search">
      <span class="search-input">SEARCH..</span>
      <svg viewBox="0 0 16 16"><circle cx="6.5" cy="6.5" r="5" fill="none" stroke="#8a8a8a" stroke-width="2"/><line x1="10.2" y1="10.2" x2="14.5" y2="14.5" stroke="#8a8a8a" stroke-width="2.4" stroke-linecap="round"/></svg>
    </div>

    <div class="quick-actions">
      <div class="quick-action" style="left:740px">
        <div class="quick-icon"><svg viewBox="0 0 16 16"><circle cx="8" cy="5" r="3.2"/><path d="M2 15c0-3.6 2.7-5.5 6-5.5s6 1.9 6 5.5z"/></svg></div>
        <div class="quick-label">Add<br>Subscribe</div>
      </div>
      <div class="quick-action" style="left:817px">
        <div class="quick-icon"><svg viewBox="0 0 16 16"><circle cx="4" cy="5" r="2.2"/><circle cx="12" cy="5" r="2.2"/><circle cx="8" cy="4" r="2.6"/><path d="M1 14c0-3 1.5-5 4-5h6c2.5 0 4 2 4 5z"/></svg></div>
        <div class="quick-label">Add<br>Participate</div>
      </div>
      <div class="quick-action" style="left:895px">
        <div class="quick-icon"><svg viewBox="0 0 16 16"><path d="M3 1h7l3 3v11H3z" fill="none" stroke="#8a8a8a" stroke-width="1.4"/><rect x="5" y="6" width="6" height="1.2"/><rect x="5" y="8.5" width="6" height="1.2"/><rect x="5" y="11" width="6" height="1.2"/></svg></div>
        <div class="quick-label">Associate<br>Surveys</div>
      </div>
    </div>

    <div class="auth auth-signin"><svg viewBox="0 0 10 10"><rect x="1" y="4.5" width="8" height="5.5" rx="1"/><path d="M2.8 4.5V3a2.2 2.2 0 0 1 4.4 0v1.5" fill="none" stroke="#fff" stroke-width="1.3"/></svg>Sign in</div>
    <div class="auth auth-signup"><svg viewBox="0 0 10 10"><path d="M1 9l.6-2.4L7 1.2 8.8 3 3.4 8.4z"/></svg>Sign Up</div>
  </header>

  <nav class="main-nav">
    <div class="nav-item is-active" style="left:99px;width:88px">HOME</div>
    <div class="nav-item" style="left:187px;width:100px">PROFILE</div>
    <div class="nav-item" style="left:287px;width:123px">RESOURCES</div>
    <div class="nav-item" style="left:410px;width:88px">NEWS</div>
    <div class="nav-item" style="left:498px;width:99px">EVENTS</div>
    <div class="nav-item is-last" style="left:597px;width:126px">CONATCT US</div>
    <div class="nav-secondary" style="left:918px">Buisness Services</div>
    <div class="nav-secondary" style="left:1052px">Upgrade</div>
  </nav>

  <section class="hero">
    <div class="hero-media" role="img" aria-label="Photo of a hand touching a phone screen with floating social media icons"></div>
    <div class="hero-copy hero-kicker">TEAMORA</div>
    <div class="hero-copy hero-title">SOCIAL MEDIA PLATFORM</div>
    <div class="hero-cta">READ MORE &gt;&gt;</div>
    <div class="hero-dots">
      <span class="hero-dot is-active"></span><span class="hero-dot"></span><span class="hero-dot"></span><span class="hero-dot"></span>
    </div>
  </section>

  <footer class="site-footer">
    <div class="copyright">Copyrights © 2015 Teamora. All Rights Reserved.</div>
    <div class="footer-links">Terms &amp; Conditions<span>|</span>Privacy Policy<span>|</span>Sitemap</div>
    <div class="social">
      <span class="social-item" aria-label="Social link 1"></span>
      <span class="social-item" aria-label="Social link 2"></span>
      <span class="social-item" aria-label="Social link 3"></span>
      <span class="social-item" aria-label="Social link 4"></span>
      <span class="social-item" aria-label="Feed link"></span>
      <span class="social-item" aria-label="Social link 5"></span>
    </div>
  </footer>
</body>
</html>
```